Gift Bag Design

We need a gift bag designed for our practice. We are a upscale optometry practice. The gift bags are given to our patients when they pick up their eyewear. We would like to see a gift bag designed with the use of dark grays and purples with a nice texture. We want simple, elegant, and upscale. We really like something with the texture of lumeca laminate frosted reed style number 4812-73. We also use chromyx 5138U for our purple colors.
Target Market(s)
Middle aged women that are fashionable
Industry/Entity Type
Eyewear
Requirements
Must have
- We must have use of our logo, which we've attached. The name of the business must be "optic haven" or "clearview optic haven", whichever works better. The dimensions of the bag must be 20.5 cm high x 12.5 cm wide x 7.5 deep.
Nice to have
- Our phone number 401-555-7316 and our website www.ClearviewOpticHavenRI.example
Should not have
- No red, yellow

```html
<!DOCTYPE html>
<html lang="en">
<head>
<meta charset="utf-8">
<title>Clearview Optic Haven — Gift Bag</title>
<link rel="stylesheet" href="https://fonts.googleapis.com/css2?family=Cormorant+Garamond:wght@500&family=Montserrat:wght@500&display=swap">
<style>
  :root {
    --paper: #ffffff;
    --plum-deep: #2a0e58;
    --plum-mid: #3b1a72;
    --lavender: #726cb0;
    --label-grey: #8a8a8a;
    --light: #ffffff;
  }
  * { margin: 0; padding: 0; box-sizing: border-box; }
  html, body { width: 1200px; height: 900px; overflow: hidden; background: var(--paper); }
  .canvas { position: relative; width: 1200px; height: 900px; background: var(--paper); }

  .bag-handle { position: absolute; left: 386px; top: 78px; width: 204px; height: 120px; }

  .bag-front {
    position: absolute; left: 298px; top: 182px; width: 370px; height: 608px;
    background: var(--lavender); overflow: hidden;
  }
  .bag-front__texture {
    position: absolute; left: 0; top: 0; width: 100%; height: 356px;
    background: linear-gradient(90deg, var(--plum-deep) 0%, var(--plum-mid) 35%, var(--plum-deep) 60%, var(--plum-mid) 85%, var(--plum-deep) 100%);
  }
  .bag-front__name {
    position: absolute; left: 0; right: 0; top: 486px; text-align: center;
    font-family: "Cormorant Garamond", serif; font-weight: 500;
    color: var(--plum-deep); font-size: 26px; line-height: 1.05; letter-spacing: 1px;
    text-transform: uppercase;
  }

  .bag-side {
    position: absolute; left: 680px; top: 182px; width: 224px; height: 608px;
    background: var(--lavender); text-align: center;
  }
  .bag-side__name {
    margin-top: 288px;
    font-family: "Cormorant Garamond", serif; font-weight: 500;
    color: var(--plum-deep); font-size: 26px; line-height: 1.05; letter-spacing: 1px;
    text-transform: uppercase;
  }
  .bag-side__contact {
    margin-top: 12px;
    font-family: "Montserrat", sans-serif; font-weight: 500;
    color: var(--light); font-size: 8.5px; line-height: 1.5; letter-spacing: 1.4px;
  }

  .view-label {
    position: absolute; top: 812px; width: 200px; text-align: center;
    font-family: "Montserrat", sans-serif; font-weight: 500;
    color: var(--label-grey); font-size: 7.5px; letter-spacing: 2px; text-transform: uppercase;
  }
  .view-label--front { left: 383px; }
  .view-label--side { left: 692px; }
</style>
</head>
<body>
<main class="canvas">
  <svg class="bag-handle" viewBox="0 0 204 120" aria-hidden="true">
    <path d="M6 120 V70 A96 64 0 0 1 198 70 V120" fill="none" stroke="var(--plum-deep)" stroke-width="6"/>
  </svg>

  <section class="bag-front" aria-label="Front view of gift bag">
    <div class="bag-front__texture" role="img" aria-label="Frosted reed vertical texture in deep plum tones"></div>
    <p class="bag-front__name">Clearview<br>Optic Haven</p>
  </section>

  <section class="bag-side" aria-label="Side view of gift bag">
    <p class="bag-side__name">Clearview<br>Optic Haven</p>
    <p class="bag-side__contact">www.ClearviewOpticHavenRI.example<br>401-555-7316</p>
  </section>

  <p class="view-label view-label--front">Front View</p>
  <p class="view-label view-label--side">Side View</p>
</main>
</body>
</html>
```